Driving School Signage Design

I need a partial/full vehicle wrap design that will stand out for my driving school and bring in as much business as my last car has, if not more! At the moment I just have a black holm corvo with very plain signage, the logo, phone number and website and some qp, quillo logos.

My new car is the latest 2013 Holm Corvo 5 door in white. It has nearly exactly the same dimensions and look on the sides as the older corvo. The front bonnet, roof and back are slightly redesigned however.

Designs can be a partial wrap, just on the sides of the vehicle and then for example lettering on the white car background. Im suggesting using something like the border of my website www.drivewithease.co.uk, the tarmac and yellow lines or a pound coin like the coins in my logo to emphasis low cost etc. But the choice is yours! It just needs to stand out well, be colourful and promote the business well and its business values of low cost driving lessons and emphasis on student discount. I am very OPEN to the idea of a full vehicle wrap if it looks good and wows me enough.

Please visit my website for inspiration www.drivewithease.co.uk and to find any information you require, or send me a message info@drivewithease.co.uk

Also see attachments for logo, picture of old car and photos of other competing driving schools in my area (the cars shown are also holm corvos)

I have also attached the car outline diagram for my current car if you cant find the 2013 vehicle outline, as it is nearly the same

Thanks

Marcus
Updates

Can all designers please post there design ideas or updated redesigns as requested ASAP please, I am going to start narrowing down the finalists in the next few days to make it easier, new submissions will still be considered all the way up to the final date however 

Thanks

Marcus

Target Market(s)

17-24 year olds, often students

Industry/Entity Type

Driving School

Requirements
Must have
• -Colourful design/stand out design
-Must involve company logo
-telephone number
-website address
-chatterly, quillo and clipvane logos
-A "student discount" sign
Nice to have
• -Design to focus heavily on core value of business, low cost driving lessons, no gimmick prices, student discount, see website to get a feel for the business
www.drivewithease.co.uk

-Involve graphics or pictures relevant to a driving school or low cost (e.g. Person holding a L plate, tarmac stone effect and yellow lines (like border of website), £1 coin to emphasise cost etc)

other things that would be great to include (if there is room):

-slogan's "No gimmick prices!" "Just a low hourly rate" "FREE online theory training"
-a QR code
Should not have
• -No signage on the windows

```html
<!DOCTYPE html>
<html lang="en">
<head>
<meta charset="utf-8">
<title>DRIVEWITHEASE driving school – vehicle side panel</title>
<link rel="stylesheet" href="https://fonts.googleapis.com/css2?family=Fredoka:wght@600&family=Nunito:wght@700;800&display=swap">
<style>
  :root {
    --border-tarmac: #8a6a4e;
    --panel-yellow: #ffd21f;
    --panel-orange: #f5a23a;
    --panel-red: #e8413a;
    --band-red: #e8413a;
    --text-white: #ffffff;
    --contact-red: #c1272d;
    --logo-blue: #29a8e0;
    --logo-red: #e8413a;
    --icon-blue: #3a7fc4;
  }
  html, body {
    margin: 0;
    padding: 0;
    width: 1200px;
    height: 325px;
    overflow: hidden;
    background: #ffffff;
  }
  .side-panel {
    position: relative;
    width: 1200px;
    height: 325px;
    font-family: "Nunito", sans-serif;
  }
  .tarmac-border {
    position: absolute;
    inset: 0;
    border-radius: 14px;
    background: var(--border-tarmac);
  }
  .panel-face {
    position: absolute;
    inset: 15px;
    border-radius: 14px;
    background: linear-gradient(90deg, var(--panel-yellow) 0%, var(--panel-orange) 60%, var(--panel-red) 100%);
    overflow: hidden;
  }
  .logo-badge {
    position: absolute;
    left: 27px;
    top: 38px;
    width: 98px;
    height: 98px;
    border-radius: 50%;
    background: var(--logo-red);
    border: 7px solid var(--logo-blue);
    box-sizing: border-box;
  }
  .brand-name {
    position: absolute;
    left: 160px;
    top: -4px;
    width: 880px;
    margin: 0;
    font-family: "Fredoka", sans-serif;
    font-weight: 600;
    font-size: 114px;
    line-height: 1.1;
    letter-spacing: 1px;
    color: var(--text-white);
    white-space: nowrap;
  }
  .service-band {
    position: absolute;
    left: 527px;
    top: 124px;
    width: 488px;
    height: 40px;
    background: var(--band-red);
  }
  .service-name {
    position: absolute;
    right: 205px;
    top: 112px;
    margin: 0;
    font-size: 46px;
    font-weight: 700;
    color: var(--text-white);
    line-height: 1;
  }
  .discount-sign {
    position: absolute;
    left: 412px;
    top: 179px;
    margin: 0;
    font-size: 27px;
    font-weight: 700;
    color: var(--text-white);
  }
  .contact-list {
    position: absolute;
    left: 36px;
    top: 182px;
    margin: 0;
    padding: 0;
    list-style: none;
    color: var(--contact-red);
    font-weight: 800;
  }
  .contact-item {
    display: flex;
    align-items: center;
    gap: 8px;
    height: 38px;
  }
  .contact-item svg { flex: none; }
  .contact-email { font-size: 17px; height: 30px; }
  .contact-phone { font-size: 25px; }
  .contact-web { font-size: 18px; }
  .social-list {
    position: absolute;
    right: 24px;
    bottom: 22px;
    margin: 0;
    padding: 0;
    list-style: none;
    display: flex;
    align-items: center;
    gap: 18px;
    font-size: 24px;
    font-weight: 800;
    color: var(--text-white);
  }
</style>
</head>
<body>
<main class="side-panel">
  <div class="tarmac-border" role="img" aria-label="Tarmac stone texture border with yellow lines and coins"></div>
  <div class="panel-face">
    <div class="logo-badge" aria-hidden="true"></div>
    <h1 class="brand-name">DRIVEWITHEASE</h1>
    <div class="service-band" aria-hidden="true"></div>
    <p class="service-name">driving school</p>
    <p class="discount-sign">A "student discount" sign</p>

    <ul class="contact-list">
      <li class="contact-item contact-email">
        <svg width="22" height="16" viewBox="0 0 22 16" aria-hidden="true">
          <rect x="1" y="1" width="20" height="14" rx="2" fill="none" stroke="var(--contact-red)" stroke-width="2"/>
          <path d="M1 2 L11 9 L21 2" fill="none" stroke="var(--contact-red)" stroke-width="2"/>
        </svg>
        info@drivewithease.co.uk
      </li>
      <li class="contact-item contact-phone">
        <svg width="30" height="30" viewBox="0 0 30 30" aria-hidden="true">
          <circle cx="15" cy="15" r="13" fill="none" stroke="var(--contact-red)" stroke-width="2.5"/>
          <path d="M10 8 C8 10 9 15 12 18 C15 21 20 22 22 20 L20 17 L17 18 C15 17 13 15 12 13 L13 10 Z" fill="var(--contact-red)"/>
        </svg>
        01632 960 960
      </li>
      <li class="contact-item contact-web">
        <svg width="28" height="28" viewBox="0 0 28 28" aria-hidden="true">
          <circle cx="14" cy="14" r="12" fill="var(--icon-blue)"/>
          <ellipse cx="14" cy="14" rx="5" ry="12" fill="none" stroke="#ffffff" stroke-width="1.5"/>
          <path d="M2 14 H26 M4 8 H24 M4 20 H24" stroke="#ffffff" stroke-width="1.5"/>
        </svg>
        www.drivewithease.co.uk
      </li>
    </ul>

    <ul class="social-list">
      <li>quillo</li>
      <li>chatterly</li>
      <li>clipvane</li>
    </ul>
  </div>
</main>
</body>
</html>
```